Birchvale Lending Business Cards

please see business card design and compass logo design. please make the blue a bit lighter

Contact Information for Business Card

Marnie Holt
Proprietor
Dip Finance & Mortgage Broking Management (this can be shortened)
LBCN
ACR *****
ABN ****
Mobile
Email

Logo Text

home, business, asset finance

Colors
ffcf3e
ffc214
33a6d7
85acd3
3277b5
ffffff

Requirements
Should not have
• pictures of oceans or cities. I am not trying to replicate a fishing company

```html
<!DOCTYPE html>
<html lang="en">
<head>
<meta charset="utf-8">
<title>Birchvale Lending — Business Cards</title>
<link rel="stylesheet" href="https://fonts.googleapis.com/css2?family=Jost:wght@400;500;700;800&display=swap">
<style>
  :root {
    --stage: #2c2c2e;
    --card-white: #ffffff;
    --brand-yellow: #ffc214;
    --brand-yellow-soft: #ffcf3e;
    --brand-blue: #3277b5;
    --brand-blue-light: #33a6d7;
    --ink: #3a3326;
  }
  * { box-sizing: border-box; margin: 0; padding: 0; }
  html, body { width: 1200px; height: 801px; overflow: hidden; }
  body {
    background: var(--stage);
    font-family: "Jost", "Futura", sans-serif;
    position: relative;
  }
  .set-title {
    position: absolute; left: 38px; top: 52px;
    color: var(--brand-yellow);
    font-size: 32px; font-weight: 400; letter-spacing: 2px;
  }
  .card {
    position: absolute;
    width: 530px; height: 303px;
    background: var(--card-white);
    box-shadow: 0 18px 40px rgba(0,0,0,.45);
    overflow: hidden;
  }
  .card--front { left: 625px; top: 170px; }
  .card--back  { left: 45px;  top: 380px; }

  /* Front */
  .front-lockup {
    position: absolute; inset: 0;
    display: flex; flex-direction: column; align-items: center; justify-content: center;
    gap: 14px;
  }
  .brand-row { display: flex; align-items: center; gap: 14px; }
  .brand-dot { width: 26px; height: 26px; border-radius: 50%; background: var(--brand-yellow); }
  .brand-name--front {
    color: var(--brand-yellow);
    font-size: 38px; font-weight: 800; letter-spacing: 3px; text-transform: uppercase;
  }
  .web-row { display: flex; align-items: center; gap: 14px; }
  .web-row svg { display: block; }
  .web-address {
    color: var(--brand-blue);
    font-size: 15px; font-weight: 500; letter-spacing: 3px; text-transform: uppercase;
  }

  /* Back */
  .yellow-panel { position: absolute; inset: 0; }
  .back-brand {
    position: absolute; left: 28px; top: 110px; width: 220px;
    display: flex; flex-direction: column; align-items: center; gap: 12px;
  }
  .brand-dot--blue { background: var(--brand-blue); width: 34px; height: 34px; border-radius: 50%; }
  .brand-name--back {
    color: var(--brand-blue);
    font-size: 23px; font-weight: 700; letter-spacing: 2px; text-transform: uppercase; text-align: center;
    line-height: 1.15;
  }
  .contact {
    position: absolute; left: 315px; top: 68px;
    color: var(--ink);
  }
  .contact__name {
    color: var(--card-white);
    font-size: 27px; font-weight: 800; letter-spacing: 1.5px; text-transform: uppercase;
  }
  .contact__role { font-size: 12px; font-weight: 500; margin-top: 2px; }
  .contact__list { list-style: none; margin-top: 28px; font-size: 15px; }
  .contact__list li { display: flex; align-items: center; gap: 9px; margin-bottom: 5px; }
  .contact__list svg { width: 13px; height: 13px; fill: var(--ink); }
  .contact__reg { font-size: 14px; margin-top: 36px; letter-spacing: .5px; }
</style>
</head>
<body>
  <div class="set-title">Business Card 3</div>

  <section class="card card--front" aria-label="Card front">
    <div class="front-lockup">
      <div class="brand-row">
        <span class="brand-dot"></span>
        <span class="brand-name--front">Birchvale Lending</span>
      </div>
      <div class="web-row">
        <svg width="100" height="10" viewBox="0 0 100 10" aria-hidden="true">
          <line x1="4" y1="5" x2="100" y2="5" stroke="#3277b5" stroke-width="2"/>
          <path d="M0 5 L7 1.5 L7 8.5 Z" fill="#3277b5"/>
        </svg>
        <span class="web-address">www.birchvalelend.com</span>
        <svg width="100" height="10" viewBox="0 0 100 10" aria-hidden="true">
          <line x1="0" y1="5" x2="96" y2="5" stroke="#3277b5" stroke-width="2"/>
          <path d="M100 5 L93 1.5 L93 8.5 Z" fill="#3277b5"/>
        </svg>
      </div>
    </div>
  </section>

  <section class="card card--back" aria-label="Card back">
    <svg class="yellow-panel" width="530" height="303" viewBox="0 0 530 303" aria-hidden="true">
      <polygon points="300,0 530,0 530,303 215,303" fill="#ffc214"/>
    </svg>

    <div class="back-brand">
      <span class="brand-dot--blue"></span>
      <span class="brand-name--back">Birchvale<br>Lending</span>
    </div>

    <div class="contact">
      <div class="contact__name">Marnie Holt</div>
      <div class="contact__role">Proprietor, LBCN</div>
      <ul class="contact__list">
        <li>
          <svg viewBox="0 0 16 16" aria-hidden="true"><path d="M3.6 1.2l2.3 2.6-1.3 2a9 9 0 0 0 5.6 5.6l2-1.3 2.6 2.3-1.4 2.2C7.5 14.7 1.3 8.5 1.4 2.6z"/></svg>
          <span>0400 218 735</span>
        </li>
        <li>
          <svg viewBox="0 0 16 16" aria-hidden="true"><path d="M1 3h14v10H1zM1.8 3.8 8 8.6l6.2-4.8" stroke="#ffc214" stroke-width="1"/></svg>
          <span>info@marnieholt.com</span>
        </li>
      </ul>
      <div class="contact__reg">ACR ***** &nbsp;|&nbsp; ABN ****</div>
    </div>
  </section>
</body>
</html>
```